The Bright Meadow Foundation

This is a non profit . We are a 501(c)(3) charitable organization in the United States. The organization is a volunteer based group providing basic healthcare to those living in underserved rural areas around the world. I have attached a brochure that provides some information about the organization. We are looking for a basic 5 page web page Page 1 Photos that fade into the next x 3 with mission statementPage 2 About us - details about bright meadow foundation. also introducing our Founders of the organization. Marina Kellet, M.D. Dorla Penn , FNP, Rosa Tembley, FNP, Wade Marlow. ( will provide you info on each.Page 3 Projects coming up and futurePage 4 Get involved - Give a donation, Volunteer, Corporate supportPage 5 Support us and contact us with a message box.We mainly work in South America but anticipate trave to South Africa in the near future. Colors bright with emphasis on Reds and Purples. I have attached some photos and ideas. You can use or not use ok to use something similar if you so like

Target Market(s)

People interested in volunteering time or money to overseas medical work. NOT a religious base

Coding

Coded - Design and coding required

Number of Pages Required

1 page

Colors
876aae
ec1f27
f37022
9bcb3c

Requirements
Must have
• Colorful pictures nature, brings out emotion, colorful, children from various parts of the world, animals.
• Tried to down load some pictures but would not go thru.

```html
<!DOCTYPE html>
<html lang="en">
<head>
<meta charset="utf-8">
<title>The Bright Meadow Foundation</title>
<link href="https://fonts.googleapis.com/css2?family=Amatic+SC:wght@700&family=Montserrat:wght@600;700&family=Open+Sans:wght@400;600;700&display=swap" rel="stylesheet">
<style>
:root{
  --purple:#7b4b9e;
  --purple-dark:#5e3681;
  --lavender:#876aae;
  --red:#e3432f;
  --red-bright:#ec1f27;
  --orange:#f37022;
  --green:#6d9a2b;
  --green-light:#9bcb3c;
  --ink:#2b2b2b;
  --muted:#6b6b6b;
  --line:#d9d9d9;
  --white:#ffffff;
}
*{box-sizing:border-box;margin:0;padding:0}
html,body{width:1200px;height:3900px;overflow:hidden}
body{position:relative;background:var(--white);font-family:'Open Sans',Arial,sans-serif;color:var(--ink)}
.display{font-family:'Amatic SC','Arial Narrow',sans-serif;font-weight:700;letter-spacing:1px}
.btn{display:inline-flex;align-items:center;gap:8px;border-radius:30px;font-family:'Montserrat',Arial,sans-serif;font-weight:600;font-size:14px;padding:9px 22px;text-decoration:none}
.btn-purple{background:var(--purple);color:var(--white)}
.btn-white{background:var(--white)}
.btn .dot{width:12px;height:12px;border-radius:50%;background:currentColor;opacity:.8}

/* hero */
.hero{position:absolute;left:0;top:0;width:1200px;height:820px}
.hero-photo{position:absolute;inset:0;background:linear-gradient(115deg,#c9a06f 0%,#d88e63 28%,#b77359 50%,#8c95a8 72%,#5f7fa8 100%)}
.hero-wave{position:absolute;left:0;bottom:0;width:1200px;height:120px}
.contact-strip{position:absolute;right:0;top:0;height:40px;width:520px;background:var(--purple);border-bottom-left-radius:24px;display:flex;align-items:center;justify-content:flex-end;gap:28px;padding-right:48px;color:var(--white);font-size:13px}
.contact-strip span{display:flex;align-items:center;gap:8px}
.brand{position:absolute;left:88px;top:40px;display:flex;align-items:center;gap:12px;color:var(--white);font-family:'Montserrat',Arial,sans-serif;font-weight:700;font-size:22px;line-height:1.1;width:260px}
.brand .mark{width:40px;height:40px;border-radius:50%;background:var(--white);opacity:.9;flex:none}
.nav{position:absolute;top:72px;left:440px;display:flex;gap:34px;align-items:center;color:var(--white);font-family:'Montserrat',Arial,sans-serif;font-size:14px;font-weight:600}
.mission{position:absolute;left:56px;top:170px;width:440px;height:440px;border-radius:50%;background:rgba(109,154,43,.93);border:6px solid var(--white);color:var(--white);text-align:center;padding:70px 56px 0}
.mission .icon{width:54px;height:54px;border-radius:50%;background:var(--white);margin:0 auto 10px}
.mission h1{font-family:'Montserrat',Arial,sans-serif;font-weight:700;font-size:44px;margin-bottom:12px}
.mission p{font-size:14px;line-height:1.55;margin-bottom:18px}
.hero-dots{position:absolute;left:250px;top:628px;display:flex;gap:8px}
.hero-dots i{width:11px;height:11px;border-radius:50%;background:rgba(255,255,255,.7)}
.hero-dots i:first-child{background:var(--green-light)}

/* cards */
.cards{position:absolute;top:850px;left:108px;width:984px;display:flex;justify-content:space-between}
.card{position:relative;width:292px;height:340px;color:var(--white);text-align:center;padding:34px 30px}
.card::before{content:"";position:absolute;inset:-10px;border:2px solid var(--line);transform:rotate(-2deg);z-index:-1}
.card.purple{background:var(--purple)}
.card.red{background:var(--red)}
.card.green{background:var(--green)}
.card .icon{width:64px;height:64px;border-radius:50%;border:2px solid var(--white);margin:0 auto 14px;display:flex;align-items:center;justify-content:center}
.card h2{font-size:40px;margin-bottom:10px}
.card p{font-size:13px;line-height:1.6;margin-bottom:20px}
.card.purple .btn{color:var(--purple)}
.card.red .btn{color:var(--red)}
.card.green .btn{color:var(--green)}

/* founders */
.founders{position:absolute;top:1272px;left:0;width:1200px;height:290px;background:var(--green);color:var(--white);padding:34px 0 0 88px}
.founders h2{font-size:58px;line-height:1}
.founders .name{font-family:'Montserrat',Arial,sans-serif;font-size:22px;font-weight:600;margin:8px 0 10px}
.founders p{width:540px;font-size:14px;line-height:1.6;margin-bottom:16px}
.founder-photo{position:absolute;left:664px;top:1240px;width:352px;height:352px;border-radius:50%;border:8px solid var(--purple);background:radial-gradient(circle at 50% 45%,#8a5b46 0%,#5a3a30 45%,#b22e2e 100%)}

/* projects */
.projects-title{position:absolute;top:1612px;left:0;width:1200px;text-align:center;color:var(--purple);font-size:64px}
.tile{position:absolute}
.feature{left:88px;top:1720px;width:564px;height:284px;background:linear-gradient(135deg,#7f9a4a,#55772c);padding:34px 40px;color:var(--white)}
.feature::after{content:"";position:absolute;inset:0;background:rgba(80,110,30,.35)}
.feature .txt{position:relative;z-index:1}
.feature h3{font-family:'Montserrat',Arial,sans-serif;font-size:22px;margin-bottom:10px}
.feature p{font-size:13px;line-height:1.6;width:440px;margin-bottom:14px}
.feature .links{display:flex;gap:10px}
.feature .links i{width:26px;height:26px;border-radius:50%;background:var(--white)}
.p1{left:680px;top:1720px;width:432px;height:284px;background:linear-gradient(140deg,#c7d6a3 0%,#cf3b2a 45%,#e6b52c 70%,#3f66b5 100%)}
.p2{left:88px;top:2032px;width:316px;height:290px;background:linear-gradient(160deg,#8a6b55 0%,#c9505a 45%,#e1c245 75%,#4d5c44 100%)}
.p3{left:432px;top:2032px;width:328px;height:290px;background:linear-gradient(180deg,#8fb2d6 0%,#dfe6ee 30%,#4f6a3b 60%,#7a4fb0 100%)}
.p4{left:784px;top:2032px;width:328px;height:290px;background:linear-gradient(180deg,#dde6ee 0%,#6c8ca6 40%,#3c5a3a 75%,#c5352a 100%)}

/* involved */
.involved{position:absolute;top:2420px;left:0;width:1200px;height:360px;background:var(--red);overflow:hidden;color:var(--white);text-align:center;padding-top:50px}
.involved .shape{position:absolute;fill:rgba(255,255,255,.07)}
.involved .icon{width:64px;height:64px;border-radius:50%;background:var(--white);margin:0 auto 12px;position:relative}
.involved h2{font-size:60px;line-height:1;margin-bottom:12px;position:relative}
.involved p{font-size:14px;line-height:1.6;width:560px;margin:0 auto 18px;position:relative}

/* support + contact */
.support{position:absolute;top:2880px;left:88px;width:440px}
.contact{position:absolute;top:2880px;left:600px;width:512px}
.section-h{font-size:50px;color:var(--ink);line-height:1;margin-bottom:18px}
.support p{font-size:14px;line-height:1.7;color:var(--muted);margin-bottom:30px}
.info{display:flex;gap:14px;align-items:flex-start;margin-bottom:22px}
.info svg{flex:none}
.info b{display:block;font-size:13px;color:var(--muted);font-weight:600}
.info span{font-size:17px;color:var(--ink)}
.field{margin-bottom:16px}
.field label{display:block;font-size:13px;font-weight:700;margin-bottom:6px}
.field .box{height:38px;border:1px solid var(--line);border-radius:4px;font-size:12px;color:#a5a5a5;padding:10px 12px}
.field .box.tall{height:92px}
.row{display:flex;gap:20px}
.row .field{flex:1}

/* footer */
.footer{position:absolute;top:3480px;left:0;width:1200px;height:360px;background:var(--purple);color:var(--white)}
.footer::before{content:"";position:absolute;left:0;top:0;width:1200px;height:10px;background:var(--purple-dark)}
.footer .brand{position:absolute;left:88px;top:130px;font-size:22px}
.socials{position:absolute;left:140px;top:210px;display:flex;gap:14px}
.socials i{width:34px;height:34px;border-radius:50%;border:2px solid rgba(255,255,255,.8)}
.col{position:absolute;top:90px}
.col h4{font-size:30px;margin-bottom:14px}
.col li{list-style:none;font-size:14px;line-height:2}
.quick{left:468px}
.fcontact{left:692px}
.fcontact .info b{color:rgba(255,255,255,.8)}
.fcontact .info span{color:var(--white);font-size:16px}
.copy{position:absolute;top:3840px;left:0;width:1200px;height:60px;display:flex;align-items:center;justify-content:space-between;padding:0 88px;font-size:13px;color:var(--muted)}
.copy .center{position:absolute;left:585px;top:16px;width:30px;height:30px;border-radius:50%;background:var(--purple)}
.copy .legal{display:flex;gap:24px}
</style>
</head>
<body>

<header class="hero">
  <div class="hero-photo" role="img" aria-label="Photo of smiling children waving at the camera"></div>
  <svg class="hero-wave" viewBox="0 0 1200 120" preserveAspectRatio="none"><path d="M0 70 C200 20 360 110 600 70 S980 10 1200 60 L1200 120 L0 120 Z" fill="#7b4b9e" opacity=".9"/><path d="M0 88 C220 40 380 125 620 86 S990 30 1200 78 L1200 120 L0 120 Z" fill="#ffffff"/></svg>
  <div class="contact-strip">
    <span><svg width="14" height="11" viewBox="0 0 14 11"><rect x="0.5" y="0.5" width="13" height="10" fill="none" stroke="#fff"/><path d="M1 1 L7 6 L13 1" fill="none" stroke="#fff"/></svg>info@brightmeadowfoundation.org</span>
    <span><svg width="12" height="12" viewBox="0 0 12 12"><path d="M2 1 L4.5 1 L5.5 3.5 L4 4.8 Q5.5 7.5 7.2 8 L8.5 6.5 L11 7.5 L11 10 Q5 11 1 3 Z" fill="#fff"/></svg>+1 555-014-2277</span>
  </div>
  <div class="brand"><span class="mark"></span>Bright Meadow Foundation</div>
  <nav class="nav">
    <span>Home</span><span>About Us</span><span>Our Founders</span><span>Projects</span><span>Get Involved</span><span>Contact Us</span>
    <svg width="16" height="16" viewBox="0 0 16 16"><circle cx="6.5" cy="6.5" r="5" fill="none" stroke="#fff" stroke-width="2"/><path d="M10.5 10.5 L15 15" stroke="#fff" stroke-width="2"/></svg>
  </nav>
  <section class="mission">
    <div class="icon"></div>
    <h1>Our Mission</h1>
    <p>The Bright Meadow Foundation was founded with the aim of bringing rural and remote families the basic medical care they need. Our vision is a world where every woman, man and child has access to care and treatment close to home.</p>
    <span class="btn btn-purple"><span class="dot"></span>Donate</span>
  </section>
  <div class="hero-dots"><i></i><i></i><i></i></div>
</header>

<section class="cards">
  <article class="card purple">
    <div class="icon"><svg width="34" height="34" viewBox="0 0 34 34" fill="none" stroke="#fff" stroke-width="2"><circle cx="17" cy="17" r="14"/><ellipse cx="17" cy="17" rx="6" ry="14"/><path d="M3 17 H31 M6 9 H28 M6 25 H28"/></svg></div>
    <h2 class="display">About Us</h2>
    <p>The foundation's vision is to see that every woman, man and child have access to basic medical care and treatment as well.</p>
    <span class="btn btn-white"><span class="dot"></span>Read More</span>
  </article>
  <article class="card red">
    <div class="icon"><svg width="34" height="34" viewBox="0 0 34 34" fill="none" stroke="#fff" stroke-width="2"><path d="M4 18 L11 12 L17 15 L23 12 L30 18 L20 26 L14 22"/></svg></div>
    <h2 class="display">Partner With Us</h2>
    <p>The foundation's vision is to see that every woman, man and child have access to basic medical care and treatment as well.</p>
    <span class="btn btn-white"><span class="dot"></span>Join Us</span>
  </article>
  <article class="card green">
    <div class="icon"><svg width="34" height="34" viewBox="0 0 34 34" fill="none" stroke="#fff" stroke-width="2"><path d="M17 30 V12 M17 18 Q9 16 9 8 Q17 9 17 18 M17 15 Q25 13 25 5 Q17 6 17 15"/></svg></div>
    <h2 class="display">Our Future</h2>
    <p>The foundation's vision is to see that every woman, man and child have access to basic medical care and treatment as well.</p>
    <span class="btn btn-white"><span class="dot"></span>Get Involved</span>
  </article>
</section>

<section class="founders">
  <h2 class="display">Our Founders</h2>
  <div class="name">DORLA PENN, FNP ( CO-FOUNDER )</div>
  <p>Dorla Penn is a Family Nurse Practitioner who is currently practicing in her home state of Colorado. Dorla has spent many years working with underserved populations and has a passion for serving in her global community. Dorla graduated from Valley State University with a Bachelor's in...</p>
  <span class="btn btn-purple"><span class="dot"></span>Read More</span>
</section>
<div class="founder-photo" role="img" aria-label="Portrait photo of co-founder Dorla Penn"></div>

<h2 class="projects-title display">Upcoming Projects</h2>
<div class="tile feature" role="img" aria-label="Photo of a green forest canopy behind the project summary">
  <div class="txt">
    <h3>Lorem Ipsum Dolor Sit Amet</h3>
    <p>There are many variations of passages of Lorem Ipsum available, but the majority have suffered alteration in some form, by injected humour.</p>
    <div class="links"><i></i><i></i></div>
  </div>
</div>
<div class="tile p1" role="img" aria-label="Photo of a red macaw parrot in the forest"></div>
<div class="tile p2" role="img" aria-label="Photo of a woman and child in colourful Andean dress"></div>
<div class="tile p3" role="img" aria-label="Photo of purple lupine flowers below snowy mountains"></div>
<div class="tile p4" role="img" aria-label="Photo of misty green mountains with a red flower"></div>

<section class="involved">
  <svg class="shape" width="1200" height="360" viewBox="0 0 1200 360"><path d="M0 360 L180 210 L360 360 Z"/><path d="M900 0 L1200 0 L1200 250 Z"/><path d="M1000 360 L1130 240 L1200 300 L1200 360 Z"/></svg>
  <div class="icon"></div>
  <h2 class="display">Get Involved With Us</h2>
  <p>It is a long established fact that a reader will be distracted by the readable content of a page when looking at its layout.</p>
  <span class="btn btn-purple"><span class="dot"></span>Donate</span>
</section>

<section class="support">
  <h2 class="section-h display">Support Us</h2>
  <p>Your donations allow us to provide medical care, health resources and supplies, and wellness education to the communities we serve. The links below are some of the ways you can donate to our organization.</p>
  <div class="info"><svg width="24" height="24" viewBox="0 0 12 12"><path d="M2 1 L4.5 1 L5.5 3.5 L4 4.8 Q5.5 7.5 7.2 8 L8.5 6.5 L11 7.5 L11 10 Q5 11 1 3 Z" fill="#7b4b9e"/></svg><div><b>Phone:</b><span>1-555-014-2277</span></div></div>
  <div class="info"><svg width="24" height="20" viewBox="0 0 14 11"><rect x="0.5" y="0.5" width="13" height="10" fill="none" stroke="#7b4b9e"/><path d="M1 1 L7 6 L13 1" fill="none" stroke="#7b4b9e"/></svg><div><b>Email:</b><span>info@brightmeadowfoundation.org</span></div></div>
  <div class="info"><svg width="24" height="24" viewBox="0 0 24 24" fill="none" stroke="#7b4b9e" stroke-width="2"><circle cx="12" cy="12" r="10"/><path d="M2 12 H22 M12 2 Q6 12 12 22 Q18 12 12 2"/></svg><div><b>Website URL:</b><span>www.brightmeadowfoundation.org</span></div></div>
</section>

<section class="contact">
  <h2 class="section-h display">Contact Us</h2>
  <div class="field"><label>Name:</label><div class="box">Enter your full name</div></div>
  <div class="row">
    <div class="field"><label>Email:</label><div class="box">Enter your email address</div></div>
    <div class="field"><label>Telephone:</label><div class="box">Enter your phone number</div></div>
  </div>
  <div class="field"><label>Message:</label><div class="box tall">Enter your message</div></div>
  <span class="btn btn-purple"><span class="dot"></span>Send Message</span>
</section>

<footer class="footer">
  <div class="brand"><span class="mark"></span>Bright Meadow Foundation</div>
  <div class="socials"><i></i><i></i><i></i></div>
  <div class="col quick">
    <h4 class="display">Quick Links</h4>
    <ul><li>Home</li><li>About Us</li><li>Our Founders</li><li>Projects</li><li>Get Involved</li><li>Contact Us</li></ul>
  </div>
  <div class="col fcontact">
    <h4 class="display">Contact</h4>
    <div class="info"><svg width="22" height="22" viewBox="0 0 12 12"><path d="M2 1 L4.5 1 L5.5 3.5 L4 4.8 Q5.5 7.5 7.2 8 L8.5 6.5 L11 7.5 L11 10 Q5 11 1 3 Z" fill="#fff"/></svg><div><b>Phone:</b><span>1-555-014-2277</span></div></div>
    <div class="info"><svg width="22" height="18" viewBox="0 0 14 11"><rect x="0.5" y="0.5" width="13" height="10" fill="none" stroke="#fff"/><path d="M1 1 L7 6 L13 1" fill="none" stroke="#fff"/></svg><div><b>Email:</b><span>info@brightmeadowfoundation.org</span></div></div>
    <div class="info"><svg width="22" height="22" viewBox="0 0 24 24" fill="none" stroke="#fff" stroke-width="2"><circle cx="12" cy="12" r="10"/><path d="M2 12 H22 M12 2 Q6 12 12 22 Q18 12 12 2"/></svg><div><b>Website URL:</b><span>www.brightmeadowfoundation.org</span></div></div>
  </div>
</footer>
<div class="copy">
  <span>© Copyright 2019 Bright Meadow Foundation</span>
  <span class="center"></span>
  <span class="legal"><span>Privacy Policy</span><span>Terms &amp; Conditions</span></span>
</div>

</body>
</html>
```